Redesign Website for Tandara Flame

I have an existing website on https://www.tandaraflame-example.com.au/ and would like to have this redesigned professionally with new content (please refer to word document). We are fire protection engineers providing fire services design expertise and engineering design to a range of different clients.

We also provide drafting services to clients in the form of completing final commissioning documentation such as 'as-installed' drawings and fire services block plans to ensure compliance with the building code and relevant Australian Standards.

Target Market(s)

Builders, Architects, Consultants, Project Managers

Industry/Entity Type

Engineering Consultant

Coding

Coded - Design and coding required

Number of Pages Required

4 page

Font styles to use
Sans Serif

Requirements
Must have
• Home and about Page, fire services design page, fire block plans page, contact us page (4 Pages).

The website colour choice must match or compliment the new company logo.
Nice to have
• Quality photos of fire services installations in buildings to Australian Standards.

A website similar to this would be ideal http://corbellpyro-example.com.au
Should not have
• Stolen licensed photos

```html
<!DOCTYPE html>
<html lang="en">
<head>
<meta charset="utf-8">
<title>Tandara Flame — Fire Protection Engineers</title>
<link rel="stylesheet" href="https://fonts.googleapis.com/css2?family=Cinzel:wght@700;900&family=Open+Sans:wght@400;600;700&family=Lato:wght@400;700&display=swap">
<style>
:root{
  --orange:#f07f1e;
  --ink:#2e2e2e;
  --text:#444;
  --light:#f3f3f3;
  --dark:#161616;
  --white:#fff;
  --line:#cfcfcf;
}
*{box-sizing:border-box;margin:0;padding:0}
html,body{width:1200px;height:3136px;overflow:hidden}
body{position:relative;font-family:"Lato",sans-serif;color:var(--text);background:var(--white)}
.abs{position:absolute}
.center{text-align:center}

/* top bar & nav */
.topbar{left:0;top:0;width:1200px;height:50px;background:#111}
.topbar .call{right:108px;top:13px;color:#ddd;font:400 18px "Open Sans",sans-serif}
.topbar .call b{color:var(--white);font-weight:700}
.nav{left:0;top:50px;width:1200px;height:102px;background:var(--white);z-index:2}
.nav a{position:absolute;top:47px;font:600 14px "Open Sans",sans-serif;color:#222;text-decoration:none;letter-spacing:.2px}
.nav a.active{color:var(--orange)}
.nav a.active::after{content:"";position:absolute;left:0;right:0;bottom:-11px;height:2px;background:var(--orange)}
.brand-badge{left:499px;top:0;width:202px;height:200px;z-index:3}
.brand-name{left:499px;top:102px;width:202px;z-index:4;font:700 21px "Open Sans",sans-serif;color:var(--orange);letter-spacing:.5px}
.brand-mark{left:582px;top:56px;width:36px;height:36px;border:3px solid var(--orange);border-radius:50%;z-index:4}

/* hero */
.hero{left:0;top:152px;width:1200px;height:643px;background:linear-gradient(100deg,#2a2a2a 0%,#4a4a48 35%,#6d6b67 60%,#3b3b3a 100%)}
.hero h1{left:0;top:330px;width:1200px;font:900 80px "Cinzel",serif;color:var(--white);letter-spacing:2px}
.hero p{left:250px;top:426px;width:700px;font:400 21px/25px "Lato",sans-serif;color:#eee;letter-spacing:.4px}
.btn-pill{display:flex;align-items:center;justify-content:center;border-radius:40px;font:700 16px "Open Sans",sans-serif;text-transform:uppercase}
.hero .cta{left:521px;top:509px;width:158px;height:54px;background:var(--white);color:var(--orange)}
.dots{left:570px;top:755px;display:flex;gap:8px}
.dots span{width:9px;height:9px;border-radius:50%;background:var(--white)}
.dots span:first-child{background:transparent;border:1.5px solid var(--white)}

/* welcome */
.welcome{left:0;top:795px;width:1200px;height:423px;background:linear-gradient(90deg,#8d8d8d,#9a9a99 40%,#929291)}
.welcome h2{left:0;top:853px;width:1200px;font:700 38px "Open Sans",sans-serif;color:var(--white)}
.welcome p{left:195px;width:810px;font:400 19.5px/27px "Lato",sans-serif;color:var(--white)}
.welcome .ghost{left:506px;top:1089px;width:188px;height:61px;border:2px solid #e6e6e6;color:var(--white);font-size:18px}

/* services */
.services{left:0;top:1218px;width:1200px;height:616px;background:var(--light)}
.services h2{left:0;top:1283px;width:1200px;font:700 37px "Open Sans",sans-serif;color:var(--ink);letter-spacing:.5px}
.card{top:1384px;width:230px;text-align:center}
.card svg{display:block;margin:0 auto}
.card h3{margin-top:14px;font:700 16.5px "Open Sans",sans-serif;color:var(--orange);white-space:nowrap}
.card p{margin-top:8px;font:400 13.5px/21.3px "Lato",sans-serif;color:#444;height:128px}
.card .more{margin:0 auto;width:160px;height:45px;border:2px solid var(--orange);color:var(--orange);font-size:16px}
.arrow{top:1470px}

/* about */
.photo-frame{left:111px;top:1907px;width:445px;height:370px;border:1px solid #ddd;background:var(--white);padding:7px}
.photo{width:100%;height:100%;background:radial-gradient(ellipse at 65% 40%,#f6c23a 0%,#e88a1f 30%,#8a5a2e 60%,#5a4c42 100%)}
.about h2{left:598px;top:1922px;font:700 37px "Open Sans",sans-serif;color:var(--ink)}
.about p{left:599px;width:490px;font:400 15.5px/23.2px "Lato",sans-serif;color:#444}
.about .cta{left:599px;top:2211px;width:153px;height:48px;background:var(--orange);color:var(--white);font-size:16px}

/* contact */
.contact{left:0;top:2349px;width:1200px;height:490px;background:var(--light)}
.contact h2{left:0;top:2408px;width:1200px;font:700 37px "Open Sans",sans-serif;color:var(--ink)}
.contact .sub{left:0;top:2458px;width:1200px;font:400 16px "Lato",sans-serif;color:#555}
.field{background:var(--white);border:1px solid var(--line);font:400 14.5px "Lato",sans-serif;color:#555;padding:12px 17px}
.contact .submit{left:525px;top:2718px;width:150px;height:57px;background:var(--orange);color:var(--white);font-size:15.5px}

/* footer */
.footer{left:0;top:2839px;width:1200px;height:297px;background:linear-gradient(180deg,#1f1f1f,#141414)}
.footer h4{top:2883px;font:700 15.5px "Open Sans",sans-serif;color:var(--white);letter-spacing:.5px}
.footer .link{font:400 13.5px "Lato",sans-serif;color:#ddd}
.footer .info{font:400 13.5px/16px "Lato",sans-serif;color:#ddd}
.social{top:2923px;width:42px;height:42px;border-radius:50%;background:#6a6a6a}
.footer .rule{left:111px;top:3088px;width:978px;height:1px;background:#444}
.footer .copy{left:111px;top:3105px;font:400 13.5px "Lato",sans-serif;color:#ccc}
.footer .legal{left:886px;top:3108px;font:400 10px "Lato",sans-serif;color:#666}
.footer .code{left:1139px;top:3106px;font:400 13px "Lato",sans-serif;color:#ccc}
</style>
</head>
<body>

<!-- header -->
<div class="abs topbar">
  <div class="abs call">
    <svg width="15" height="15" viewBox="0 0 24 24" style="vertical-align:-2px"><path fill="#ddd" d="M6.6 10.8c1.4 2.8 3.8 5.1 6.6 6.6l2.2-2.2c.3-.3.7-.4 1-.2 1.1.4 2.3.6 3.6.6.6 0 1 .4 1 1V20c0 .6-.4 1-1 1C10.6 21 3 13.4 3 4c0-.6.4-1 1-1h3.5c.6 0 1 .4 1 1 0 1.3.2 2.5.6 3.6.1.3 0 .7-.2 1z"/></svg>
    Call Us: <b>+614 00 555 019</b>
  </div>
</div>
<nav class="abs nav">
  <a class="active" style="left:122px">HOME</a>
  <a style="left:220px">ABOUT</a>
  <a style="left:323px">FIRE SERVICES PLANS</a>
  <a style="left:803px">FIRE BLOCK PLANS</a>
  <a style="left:987px">CONTACT US</a>
</nav>
<svg class="abs brand-badge" viewBox="0 0 202 200"><polygon points="0,0 202,0 178,50 202,152 176,200 26,200 0,152 24,50" fill="#fff"/></svg>
<div class="abs brand-mark"></div>
<div class="abs brand-name center">TANDARA FLAME</div>

<!-- hero -->
<section class="abs hero" role="img" aria-label="Photo of a worker in a white protective suit and respirator inspecting a fire-damaged, soot-covered room"></section>
<h1 class="abs center" style="left:0;top:330px;width:1200px;font:900 80px 'Cinzel',serif;color:#fff;letter-spacing:2px">TANDARA FLAME</h1>
<p class="abs center" style="left:250px;top:426px;width:700px;font:400 21px/25px 'Lato',sans-serif;color:#eee;letter-spacing:.4px">We are fire protection engineers providing fire services design expertise and engineering design to a range of different clients.</p>
<div class="abs btn-pill" style="left:521px;top:509px;width:158px;height:54px;background:#fff;color:var(--orange)">Contact Us</div>
<div class="abs dots"><span></span><span></span><span></span><span></span></div>

<!-- welcome -->
<section class="abs welcome" role="img" aria-label="Faded photo of a grey tiled interior wall"></section>
<h2 class="abs center" style="left:0;top:853px;width:1200px;font:700 38px 'Open Sans',sans-serif;color:#fff">WELCOME TO TANDARA FLAME</h2>
<p class="abs center" style="left:195px;top:905px;width:810px;font:400 19.5px/27px 'Lato',sans-serif;color:#fff">Tandara Flame can assist with the preparation of the design and specification for the upgrade or installation or new fire safety systems to achieve compliance with the National Construction Code (NCC), Council Fire Orders or Fire Engineering Reports</p>
<p class="abs center" style="left:195px;top:999px;width:810px;font:400 19.5px/27px 'Lato',sans-serif;color:#fff">We have proficient knowledge in the ability to produce design and specifications relating to the below fire safety measures</p>
<div class="abs btn-pill" style="left:506px;top:1089px;width:188px;height:61px;border:2px solid #e6e6e6;color:#fff;font-size:18px">Learn More</div>

<!-- services -->
<section class="abs services"></section>
<h2 class="abs center" style="left:0;top:1283px;width:1200px;font:700 37px 'Open Sans',sans-serif;color:var(--ink);letter-spacing:.5px">FIRE SERVICES DRAWINGS AND BLOCK PLANS</h2>

<svg class="abs arrow" style="left:44px" width="30" height="44" viewBox="0 0 30 44"><polyline points="24,4 6,22 24,40" fill="none" stroke="#9a9a9a" stroke-width="4"/></svg>
<svg class="abs arrow" style="left:1116px" width="30" height="44" viewBox="0 0 30 44"><polyline points="6,4 24,22 6,40" fill="none" stroke="#9a9a9a" stroke-width="4"/></svg>

<div class="abs card" style="left:106px">
  <svg width="155" height="133" viewBox="0 0 155 133"><polygon points="39,3 116,3 152,66.5 116,130 39,130 3,66.5" fill="none" stroke="#f07f1e" stroke-width="5"/>
    <g fill="none" stroke="#f07f1e" stroke-width="2.5"><rect x="58" y="44" width="30" height="38"/><rect x="68" y="38" width="30" height="38" fill="#f3f3f3"/><line x1="74" y1="48" x2="92" y2="48"/><line x1="74" y1="55" x2="92" y2="55"/><line x1="74" y1="62" x2="92" y2="62"/><circle cx="70" cy="84" r="9" fill="#f3f3f3"/><circle cx="70" cy="84" r="3"/></g></svg>
  <h3>ZONE BLOCK PLANS</h3>
  <p>AS1670.1 requires an automatic smoke detection and alarm system to incorporate a Zone Block Plan to be securely mounted and easily accessible at the Fire Brigade Panel (FBP).</p>
  <div class="btn-pill more">Learn More</div>
</div>

<div class="abs card" style="left:360px">
  <svg width="155" height="133" viewBox="0 0 155 133"><polygon points="39,3 116,3 152,66.5 116,130 39,130 3,66.5" fill="none" stroke="#f07f1e" stroke-width="5"/>
    <g fill="none" stroke="#f07f1e" stroke-width="2.5"><rect x="46" y="62" width="36" height="26"/><polyline points="46,62 64,50 82,62"/><rect x="82" y="70" width="16" height="18"/><rect x="96" y="38" width="8" height="38"/><line x1="52" y1="70" x2="58" y2="70"/><line x1="64" y1="70" x2="70" y2="70"/><line x1="52" y1="78" x2="58" y2="78"/><line x1="64" y1="78" x2="70" y2="78"/><rect x="90" y="84" width="18" height="8"/></g></svg>
  <h3>EWIS / SSISEP BLOCK PLANS</h3>
  <p>AS1670.4 requires an Emergency Warning and Intercom System (EWIS) / Sound System and Intercom System for Emergency Purposes (SSISEP) to incorporate a EWIS/SSISEP Block Plan.</p>
  <div class="btn-pill more">Learn More</div>
</div>

<div class="abs card" style="left:615px">
  <svg width="155" height="133" viewBox="0 0 155 133"><polygon points="39,3 116,3 152,66.5 116,130 39,130 3,66.5" fill="none" stroke="#f07f1e" stroke-width="5"/>
    <g fill="none" stroke="#f07f1e" stroke-width="2.5"><rect x="46" y="42" width="62" height="48"/><rect x="51" y="47" width="52" height="38"/><line x1="72" y1="47" x2="72" y2="70"/><line x1="72" y1="70" x2="86" y2="70"/><line x1="86" y1="55" x2="103" y2="55"/><line x1="60" y1="60" x2="60" y2="85"/></g></svg>
  <h3>SPRINKLER BLOCK PLANS</h3>
  <p>AS2118.1 requires Automatic Fire Sprinkler Systems to incorporate a Sprinkler Block Plan to be located adjacent to each set or group of installation control assemblies and located such that it is readily.</p>
  <div class="btn-pill more">Learn More</div>
</div>

<div class="abs card" style="left:870px">
  <svg width="155" height="133" viewBox="0 0 155 133"><polygon points="39,3 116,3 152,66.5 116,130 39,130 3,66.5" fill="none" stroke="#f07f1e" stroke-width="5"/>
    <g fill="none" stroke="#f07f1e" stroke-width="2.5"><line x1="44" y1="40" x2="112" y2="40"/><rect x="70" y="40" width="16" height="12"/><rect x="73" y="52" width="10" height="10"/></g>
    <g stroke="#f07f1e" stroke-width="1.5" stroke-dasharray="3 3"><line x1="78" y1="64" x2="78" y2="96"/><line x1="74" y1="64" x2="62" y2="94"/><line x1="82" y1="64" x2="94" y2="94"/></g></svg>
  <h3>FIRE HYDRANT BLOCK PLANS</h3>
  <p>AS2419.1 requires Fire Hydrant Systems to incorporate a Fire Hydrant Block Plan to be located at the location of fire brigade booster assemblies, fire control rooms and pump rooms.</p>
  <div class="btn-pill more">Learn More</div>
</div>

<!-- about -->
<div class="abs photo-frame"><div class="photo" role="img" aria-label="Photo of a person spraying a red fire extinguisher at a blazing fire"></div></div>
<h2 class="abs" style="left:598px;top:1922px;font:700 37px 'Open Sans',sans-serif;color:var(--ink)">ABOUT TANDARA FLAME</h2>
<p class="abs" style="left:599px;top:1970px;width:490px;font:400 15.5px/23.2px 'Lato',sans-serif;color:#444">Tandara Flame is a company based in Sydney, Australia providing the Australian market expertise in the field of fire safety. Our mission is to assist our clients with the preparation of design and specifications of fire services upgrades and final commissioning documentation to achieve compliance with the National Construction Code (NCC) and relevant Australian Standards.</p>
<p class="abs" style="left:599px;top:2113px;width:490px;font:400 15.5px/23.2px 'Lato',sans-serif;color:#444">We can also assist with the review and endorsement of fire services design required under the new fire safety reforms which came into effect on July 2017.</p>
<div class="abs btn-pill" style="left:599px;top:2211px;width:153px;height:48px;background:var(--orange);color:#fff">Learn More</div>

<!-- contact -->
<section class="abs contact"></section>
<h2 class="abs center" style="left:0;top:2408px;width:1200px;font:700 37px 'Open Sans',sans-serif;color:var(--ink)">CONTACT US</h2>
<div class="abs center" style="left:0;top:2460px;width:1200px;font:400 16px 'Lato',sans-serif;color:#555">Please use the contact form below to get in touch.</div>
<div class="abs field" style="left:111px;top:2508px;width:316px;height:44px">Your Name</div>
<div class="abs field" style="left:442px;top:2508px;width:316px;height:44px">Your Email</div>
<div class="abs field" style="left:773px;top:2508px;width:316px;height:44px">Your Phone</div>
<div class="abs field" style="left:111px;top:2567px;width:978px;height:119px">Your Message</div>
<div class="abs btn-pill" style="left:525px;top:2718px;width:150px;height:57px;background:var(--orange);color:#fff;font-size:15.5px">Submit Now</div>

<!-- footer -->
<footer class="abs footer"></footer>
<h4 class="abs" style="left:111px;top:2883px;font:700 15.5px 'Open Sans',sans-serif;color:#fff;letter-spacing:.5px">QUICK LINKS</h4>
<h4 class="abs" style="left:522px;top:2883px;font:700 15.5px 'Open Sans',sans-serif;color:#fff;letter-spacing:.5px">CONTACT INFO</h4>
<h4 class="abs" style="left:901px;top:2883px;font:700 15.5px 'Open Sans',sans-serif;color:#fff;letter-spacing:.5px">CONNECT WITH US</h4>

<div class="abs link" style="left:112px;top:2932px;font:400 13.5px 'Lato',sans-serif;color:#ddd">Home</div>
<div class="abs link" style="left:112px;top:2962px;font:400 13.5px 'Lato',sans-serif;color:#ddd">About</div>
<div class="abs link" style="left:112px;top:2992px;font:400 13.5px 'Lato',sans-serif;color:#ddd">Fire Services Plans</div>
<div class="abs link" style="left:112px;top:3022px;font:400 13.5px 'Lato',sans-serif;color:#ddd">Fire Block Plans</div>
<div class="abs link" style="left:326px;top:2932px;font:400 13.5px 'Lato',sans-serif;color:#ddd">Terms of Use</div>
<div class="abs link" style="left:326px;top:2962px;font:400 13.5px 'Lato',sans-serif;color:#ddd">Privacy Policy</div>
<div class="abs link" style="left:326px;top:2992px;font:400 13.5px 'Lato',sans-serif;color:#ddd">Contact</div>
<div class="abs link" style="left:326px;top:3022px;font:400 13.5px 'Lato',sans-serif;color:#ddd">Site Map</div>

<svg class="abs" style="left:523px;top:2934px" width="10" height="14" viewBox="0 0 10 14"><path fill="#ddd" d="M5 0a5 5 0 0 0-5 5c0 4 5 9 5 9s5-5 5-9a5 5 0 0 0-5-5zm0 7a2 2 0 1 1 0-4 2 2 0 0 1 0 4z"/></svg>
<div class="abs" style="left:541px;top:2932px;width:240px;font:400 13.5px/16px 'Lato',sans-serif;color:#ddd">Tandara Flame, Street Name, City, Country Code.</div>
<svg class="abs" style="left:523px;top:2987px" width="12" height="12" viewBox="0 0 24 24"><path fill="#ddd" d="M6.6 10.8c1.4 2.8 3.8 5.1 6.6 6.6l2.2-2.2c.3-.3.7-.4 1-.2 1.1.4 2.3.6 3.6.6.6 0 1 .4 1 1V20c0 .6-.4 1-1 1C10.6 21 3 13.4 3 4c0-.6.4-1 1-1h3.5c.6 0 1 .4 1 1 0 1.3.2 2.5.6 3.6.1.3 0 .7-.2 1z"/></svg>
<div class="abs" style="left:541px;top:2985px;font:700 13px 'Lato',sans-serif;color:#ddd">+614 00 555 019</div>
<svg class="abs" style="left:523px;top:3024px" width="13" height="10" viewBox="0 0 13 10"><rect width="13" height="10" rx="1" fill="#ddd"/><polyline points="0,1 6.5,6 13,1" fill="none" stroke="#1a1a1a" stroke-width="1.2"/></svg>
<div class="abs" style="left:541px;top:3021px;font:700 13px 'Lato',sans-serif;color:#ddd">info@tandaraflame-example.com.au</div>

<div class="abs social" style="left:901px" role="img" aria-label="Social profile link"></div>
<div class="abs social" style="left:950px" role="img" aria-label="Social profile link"></div>
<div class="abs social" style="left:998px" role="img" aria-label="Social profile link"></div>
<div class="abs social" style="left:1047px" role="img" aria-label="Social profile link"></div>

<div class="abs" style="left:111px;top:3088px;width:978px;height:1px;background:#444"></div>
<div class="abs" style="left:111px;top:3105px;font:400 13.5px 'Lato',sans-serif;color:#ccc">Copyrights © 2021 Tandara Flame. All rights reserved.</div>
<div class="abs" style="left:886px;top:3108px;font:400 10px 'Lato',sans-serif;color:#666">Terms and Conditions | Privacy Policy</div>
<div class="abs" style="left:1139px;top:3106px;font:400 13px 'Lato',sans-serif;color:#ccc">C16</div>

</body>
</html>
```